WebDesign | Financial Services Firm - Risk Mitigation

We are a professional services consulting firm that specializes in high net worth individuals over $25,000,000, executives C-suite and above, closely held businesses owners, family offices and highly compensated employees.

Our focus is on risk mitigation and tax efficient strategies. Our clients take their risk on themselves and have a proven track record generating wealth. Our directive is to preserve and protect the wealth they’ve already created.

Our company Harbor Crest Advisory is geared around five directives of asset protection:
1) Legal Structuring
2) Leverage & Financing
3) Risk Management - Asset Protection & Insurance, Trustee Work
4) Asset Management & Investing - Under www.tqlvalemark.com
5) Tax Efficient Strategies

Our Company Mark is a Pentagon with a key in the middle. A pentagon is the most efficient defensive structure. Each point of a pentagon is equal distance front every point . Each side provides support to another and works together, which is the key to our clients success.

Our key colors are blue, black and silver.

We ‘re located in the Pacific Northwest with bi coastal and international clients. We have fewer, higher net worth clients and provide exceptional customer service. We do not do social media.

We'll need the following pages:
-Front Landing Page.
Front page has to have link to hbportal.docuvaultix.com for logging into secure site.
- Contact & About Us Page
- Our Team Page
- Five Sides of Wealth Management
> Legal & Business Structuring
> Leverage & Financing
> Risk Management & Asset Protection.
> Asset Management and Investing - Will link to TQL (won't be turned on for a few months)
> Tax Efficient Strategies.

Industry/Entity Type

Financial Service

Coding

Coded - Design and coding required

Number of Pages Required

5+ page

Font styles to use
Sans Serif

Colors
0555a3

Requirements
Must have
• Our key colors are blue, black and silver.

-Front Landing Page.
- Contact & About Us Page
- Our Team Page
> Leverage & Financing
Nice to have
• I have attached images that have been purchased for use on the webpage. Us or not.

location page: 847 W Alder Ln, Suite 412, Lake Oswego, OR 97035
Should not have
• lots of color.

```html
<!DOCTYPE html>
<html lang="en">
<head>
<meta charset="utf-8">
<title>Harbor Crest Advisory — Risk Mitigation &amp; Tax Efficient Strategies</title>
<link href="https://fonts.googleapis.com/css2?family=Crimson+Pro:wght@600;700&family=Poppins:wght@400;500&family=Rubik:wght@700&family=Roboto:wght@400&display=swap" rel="stylesheet">
<style>
:root{
  --blue:#0555a3;
  --blue-bright:#1a8fd6;
  --navy:#0c2a6b;
  --ink:#050b1a;
  --text:#555b66;
  --silver:#e8edf3;
  --white:#fff;
}
*{margin:0;padding:0;box-sizing:border-box}
html,body{width:1200px;height:3150px;overflow:hidden}
body{position:relative;background:var(--white);font-family:"Poppins",sans-serif;color:var(--text)}
.abs{position:absolute}

/* header */
.brand{left:60px;top:14px;display:flex;align-items:center;gap:12px}
.brand-dot{width:46px;height:46px;border-radius:50%;background:var(--navy)}
.brand-name{font-family:"Crimson Pro",serif;font-weight:700;font-size:25px;color:var(--navy);letter-spacing:.5px;line-height:1}
.nav{right:220px;top:31px;display:flex;gap:22px;font-size:12.5px;color:#222}
.nav .active{color:var(--blue-bright);display:flex;align-items:center;gap:5px}
.btn{display:flex;align-items:center;justify-content:space-between;border-radius:22px;background:linear-gradient(90deg,var(--blue-bright),var(--blue));color:#fff;font-family:"Crimson Pro",serif;font-weight:700;font-size:17px;letter-spacing:.5px;padding:0 4px 0 22px}
.btn-dot{width:32px;height:32px;border-radius:50%;background:#fff;border:3px solid var(--navy)}
.login{left:1017px;top:20px;width:124px;height:37px}

/* hero */
.hero{left:0;top:75px;width:1200px;height:630px;clip-path:polygon(0 0,100% 0,100% 580px,0 630px);
  background:linear-gradient(180deg,#6f7c8e 0%,#8b8677 35%,#5b4a3a 62%,#3a3a40 100%)}
.hero-shade{left:0;top:75px;width:700px;height:630px;background:linear-gradient(90deg,rgba(20,25,35,.55),rgba(20,25,35,0));clip-path:polygon(0 0,100% 0,100% 588px,0 630px)}
.hero-title{left:120px;top:248px;width:520px;font-family:"Rubik",sans-serif;font-weight:700;font-size:40px;line-height:45px;color:#fff;text-transform:uppercase}
.hero-sub{left:121px;top:392px;width:440px;font-family:"Roboto",sans-serif;font-size:14.5px;line-height:21px;color:#fff}
.hero-cta{left:120px;top:448px;width:175px;height:38px}
.arrow{width:44px;height:44px;top:321px}

/* headings */
.eyebrow{width:1200px;left:0;text-align:center;font-size:16px;color:var(--blue-bright)}
.title{left:0;width:1200px;display:flex;justify-content:center;align-items:center;gap:8px;font-family:"Crimson Pro",serif;font-weight:700;font-size:31px;color:var(--navy);text-transform:uppercase;letter-spacing:.5px}
.title::before,.title::after{content:"";width:48px;height:2px;background:currentColor}

/* about */
.about-copy{left:340px;top:848px;width:520px;text-align:center;font-size:11.5px;line-height:19.5px}
.about-copy p+p{margin-top:10px}
.about-cta{left:503px;top:1013px;width:194px;height:38px}

/* services */
.band-services{left:0;top:1110px;width:1200px;height:780px;clip-path:polygon(0 50px,100% 0,100% 730px,0 780px);background:linear-gradient(180deg,#eef2f6,#e3e9ef 60%,#eaeef3)}
.svc-name{font-family:"Crimson Pro",serif;font-weight:700;font-size:18px;color:var(--navy)}
.svc-text{font-size:11.5px;line-height:19.5px;color:#333}
.svc-right{text-align:right}

/* team */
.member-photo{width:210px;height:262px}
.member-frame{width:210px;height:262px;background:#d9eef8}
.member-name{font-family:"Crimson Pro",serif;font-weight:700;font-size:22px;color:var(--navy)}
.member-bio{width:225px;font-size:11.5px;line-height:19.5px}
.member-bio p+p{margin-top:10px}
.member-link{font-family:"Crimson Pro",serif;font-weight:700;font-size:12px;color:var(--blue-bright);text-decoration:underline;letter-spacing:.3px}

/* contact */
.band-contact{left:0;top:2378px;width:1200px;height:482px;clip-path:polygon(0 52px,100% 0,100% 100%,0 100%);background:linear-gradient(180deg,#1b78c8 0%,#0d5cab 45%,#0a3f86 100%)}
.field{background:#fff;border-radius:8px;font-size:10px;color:#666;padding:12px 12px;height:37px}
.submit{left:533px;top:2713px;width:134px;height:38px}

/* footer */
.footer{left:0;top:2815px;width:1200px;height:335px;clip-path:polygon(0 45px,100% 0,100% 100%,0 100%);background:var(--ink)}
.foot-head{font-family:"Crimson Pro",serif;font-weight:600;font-size:14px;color:var(--blue-bright);display:flex;align-items:center;gap:6px;text-transform:uppercase}
.foot-head::after{content:"";width:34px;height:1px;background:var(--blue-bright)}
.foot-list{list-style:none;font-size:11.5px;color:#dfe5ee}
.foot-list li{height:24px;display:flex;align-items:center;gap:12px}
.foot-list li::before{content:"";width:6px;height:6px;border-radius:50%;border:1px solid var(--blue-bright);flex:none}
.contact-row{display:flex;gap:16px;font-size:11.5px;line-height:18px;color:#dfe5ee}
.copyright{left:0;top:3118px;width:1200px;text-align:center;font-size:11px;color:#dfe5ee}
.copyright span{color:var(--blue-bright)}
</style>
</head>
<body>

<!-- header -->
<div class="abs brand"><span class="brand-dot"></span><span class="brand-name">HARBOR CREST<br>ADVISORY</span></div>
<nav class="abs nav">
  <span class="active"><svg width="13" height="13" viewBox="0 0 12 12"><path d="M1 6 6 1.5 11 6M2.5 5v5.5h7V5" fill="none" stroke="#1a8fd6" stroke-width="1.4"/></svg>Home</span>
  <span>About Us</span><span>Wealth Management</span><span>Contact Us</span>
</nav>
<a class="abs btn login">LOGIN<span class="btn-dot"></span></a>

<!-- hero -->
<div class="abs hero" role="img" aria-label="Stone and timber office building at dusk with autumn trees and a rock fountain"></div>
<div class="abs hero-shade"></div>
<svg class="abs" style="left:0;top:645px" width="1200" height="70" viewBox="0 0 1200 70"><polygon points="0,60 1200,10 1200,18 0,66" fill="#0a6cc4"/></svg>
<svg class="abs arrow" style="left:38px" viewBox="0 0 44 44"><rect x="8" y="8" width="28" height="28" transform="rotate(45 22 22)" fill="rgba(0,0,0,.45)"/><path d="M25 15 18 22 25 29" fill="none" stroke="#fff" stroke-width="1.5"/></svg>
<svg class="abs arrow" style="left:1118px" viewBox="0 0 44 44"><rect x="8" y="8" width="28" height="28" transform="rotate(45 22 22)" fill="rgba(0,0,0,.45)"/><path d="M19 15 26 22 19 29" fill="none" stroke="#fff" stroke-width="1.5"/></svg>
<h1 class="abs hero-title">Risk Mitigation &amp; Tax<br>Efficient Strategies<br>Consulting Firm</h1>
<p class="abs hero-sub">Our clients take their risk on themselves and have a proven track record generating wealth</p>
<a class="abs btn hero-cta">CONTACT US<span class="btn-dot"></span></a>

<!-- about -->
<div class="abs eyebrow" style="top:762px">About</div>
<h2 class="abs title" style="top:786px">Harbor Crest Advisory</h2>
<div class="abs about-copy">
  <p>Lorem Ipsum is simply dummy text of the printing and typesetting industry. Lorem Ipsum has been the industry's standard dummy text ever since the 1500s, when an unknown printer took a galley of type and scrambled.</p>
  <p>Lorem Ipsum is simply dummy text of the printing and typesetting industry. Lorem Ipsum has been the industry's standard dummy text ever since the 1500s, when an unknown printer took a galley of type and scrambled it to make a type specimen book. It has survived not only five centuries, but also the leap into electronic</p>
</div>
<a class="abs btn about-cta">EXPLORE MORE<span class="btn-dot"></span></a>

<!-- services -->
<div class="abs band-services" role="img" aria-label="Faint background of stacked coins and banknotes"></div>
<div class="abs eyebrow" style="top:1199px">Services We Provide</div>
<h2 class="abs title" style="top:1224px">Wealth Management</h2>

<svg class="abs" style="left:0;top:1380px" width="1200" height="420" viewBox="0 0 1200 420">
  <g fill="none" stroke="#4aa8e0" stroke-width="1" stroke-dasharray="2 3">
    <path d="M600 60V150"/>
    <path d="M395 176H460L508 222"/>
    <path d="M805 176H735L692 222"/>
    <path d="M395 375H480L540 326"/>
    <path d="M805 375H720L660 326"/>
  </g>
  <circle cx="600" cy="230" r="88" fill="#0c2a6b"/>
  <circle cx="600" cy="230" r="70" fill="#fff"/>
  <circle cx="600" cy="230" r="54" fill="#1a7fcf"/>
  <g fill="#fff" stroke="#1a8fd6" stroke-width="1.5">
    <circle cx="600" cy="150" r="4"/><circle cx="508" cy="222" r="4"/><circle cx="692" cy="222" r="4"/><circle cx="540" cy="326" r="4"/><circle cx="660" cy="326" r="4"/>
  </g>
  <g>
    <circle cx="600" cy="60" r="46" fill="#0c2a6b"/><circle cx="600" cy="60" r="38" fill="#fff"/>
    <rect x="584" y="42" width="32" height="36" rx="2" fill="none" stroke="#0c2a6b" stroke-width="2"/><path d="M590 52h20M590 60h20M590 68h12" stroke="#0c2a6b" stroke-width="2"/>
  </g>
  <g>
    <circle cx="350" cy="155" r="48" fill="#0c2a6b"/><circle cx="350" cy="155" r="40" fill="#1a7fcf"/>
    <rect x="336" y="137" width="26" height="34" rx="2" fill="none" stroke="#fff" stroke-width="2"/><path d="M341 147h16M341 155h16M341 163h10" stroke="#fff" stroke-width="2"/>
  </g>
  <g>
    <circle cx="850" cy="155" r="48" fill="#0c2a6b"/><circle cx="850" cy="155" r="40" fill="#1a7fcf"/>
    <circle cx="850" cy="155" r="14" fill="none" stroke="#fff" stroke-width="2"/><circle cx="850" cy="155" r="4" fill="#fff"/>
  </g>
  <g>
    <circle cx="350" cy="355" r="48" fill="#0c2a6b"/><circle cx="350" cy="355" r="40" fill="#1a7fcf"/>
    <path d="M336 343v16M330 353l6 6 6-6" fill="none" stroke="#fff" stroke-width="2"/><circle cx="358" cy="360" r="10" fill="none" stroke="#fff" stroke-width="2"/>
  </g>
  <g>
    <circle cx="850" cy="355" r="48" fill="#0c2a6b"/><circle cx="850" cy="355" r="40" fill="#1a7fcf"/>
    <rect x="834" y="340" width="32" height="30" rx="2" fill="none" stroke="#fff" stroke-width="2"/><path d="M840 363v-6M848 363v-12M856 363v-9" stroke="#fff" stroke-width="2"/>
  </g>
</svg>

<div class="abs svc-name" style="left:450px;top:1287px;width:300px;text-align:center;line-height:22px">Asset Management &amp;<br>Investing</div>
<p class="abs svc-text" style="left:450px;top:1337px;width:300px;text-align:center">Lorem Ipsum is simply dummy text of the printing and typesetting industry.</p>

<div class="abs svc-name svc-right" style="left:77px;top:1505px;width:200px">Legal Structuring</div>
<p class="abs svc-text svc-right" style="left:97px;top:1535px;width:180px">Lorem Ipsum is simply dummy text of the printing &amp; type.</p>
<div class="abs svc-name svc-right" style="left:77px;top:1701px;width:200px">Leverage &amp; Financing</div>
<p class="abs svc-text svc-right" style="left:97px;top:1730px;width:180px">Lorem Ipsum is simply dummy text of the printing &amp; type.</p>

<div class="abs svc-name" style="left:925px;top:1505px">Risk Management</div>
<p class="abs svc-text" style="left:925px;top:1535px;width:185px">Lorem Ipsum is simply dummy text of the printing &amp; type.</p>
<div class="abs svc-name" style="left:925px;top:1703px">Tax Efficient Strategies</div>
<p class="abs svc-text" style="left:929px;top:1730px;width:185px">Lorem Ipsum is simply dummy text of the printing &amp; type.</p>

<!-- team -->
<div class="abs eyebrow" style="top:1930px">Meet Experts</div>
<h2 class="abs title" style="top:1955px">Our Team</h2>

<div class="abs member-frame" style="left:72px;top:2054px"></div>
<div class="abs member-photo" style="left:60px;top:2042px;background:linear-gradient(180deg,#5c5a58,#6b4f3c 45%,#4a46c4 75%,#3d3bb0)" role="img" aria-label="Portrait of Marcus Ellery in a cap and sunglasses"></div>
<div class="abs member-name" style="left:320px;top:2060px">Marcus Ellery</div>
<div class="abs member-bio" style="left:320px;top:2097px">
  <p>Marcus Ellery is the Financial Strategist &amp; Founder who partners with C-Suite Executives, Family Offices, Real Estate Investors &amp; Closely Held Business Owners to protect &amp; maximize their wealth.</p>
  <p>After spending 15 years in the commercial banking and wealth..</p>
</div>
<div class="abs member-link" style="left:321px;top:2280px">EXPLORE MORE »</div>

<div class="abs member-frame" style="left:612px;top:2054px"></div>
<div class="abs member-photo" style="left:600px;top:2042px;background:linear-gradient(180deg,#8fb07a,#6f9466 40%,#3e4650 75%,#2e3440)" role="img" aria-label="Portrait of Grant Holloway in a suit, outdoors"></div>
<div class="abs member-name" style="left:858px;top:2060px">Grant Holloway</div>
<div class="abs member-bio" style="left:858px;top:2097px">
  <p>Grant Holloway is the CFO &amp; Strategist for our closely held businesses. As a former CPA, he takes in-depth roles in closely held companies as a financial consultant during times of exit or transition.</p>
  <p>As a Key Executive, Grant Holloway, is noted for integrating new financial..</p>
</div>
<div class="abs member-link" style="left:859px;top:2280px">EXPLORE MORE »</div>

<!-- contact -->
<div class="abs band-contact" role="img" aria-label="Blue-toned view of the office building and trees"></div>
<div class="abs eyebrow" style="top:2470px;color:#2aa3e8">Get In Touch</div>
<h2 class="abs title" style="top:2495px;color:#fff">Contact Us</h2>
<div class="abs field" style="left:241px;top:2575px;width:232px">Name *</div>
<div class="abs field" style="left:484px;top:2575px;width:232px">Email *</div>
<div class="abs field" style="left:727px;top:2575px;width:232px;display:flex;justify-content:space-between">Services *<svg width="10" height="8" viewBox="0 0 10 8" style="margin-top:4px"><path d="M0 1h10L5 7z" fill="#222"/></svg></div>
<div class="abs field" style="left:241px;top:2627px;width:718px;height:75px">Message *</div>
<a class="abs btn submit">SUBMIT<span class="btn-dot"></span></a>

<!-- footer -->
<div class="abs footer"></div>
<div class="abs" style="left:65px;top:2960px;display:flex;align-items:center;gap:12px"><span class="brand-dot" style="width:56px;height:56px"></span><span class="brand-name" style="color:#2a6fd0;font-size:24px">HARBOR CREST<br>ADVISORY</span></div>

<div class="abs foot-head" style="left:337px;top:2906px">Sitemap</div>
<ul class="abs foot-list" style="left:337px;top:2940px">
  <li>Home</li><li>About Us</li><li>Wealth Management</li><li>Contact Us</li>
</ul>

<div class="abs foot-head" style="left:612px;top:2906px">Services</div>
<ul class="abs foot-list" style="left:612px;top:2940px">
  <li>Legal &amp; Business Structuring</li><li>Leverage &amp; Financing</li><li>Risk Management &amp; Asset Protection.</li><li>Asset Management &amp; Investing</li><li>Tax Efficient Strategies.</li>
</ul>

<div class="abs foot-head" style="left:887px;top:2906px">Contact Us</div>
<div class="abs contact-row" style="left:887px;top:2946px">
  <svg width="14" height="20" viewBox="0 0 14 20"><path d="M7 1a6 6 0 0 0-6 6c0 5 6 12 6 12s6-7 6-12a6 6 0 0 0-6-6z" fill="none" stroke="#1a8fd6" stroke-width="1.6"/><circle cx="7" cy="7" r="2.2" fill="#1a8fd6"/></svg>
  <span style="width:200px">847 W Alder Ln, Suite 412, Lake Oswego, OR 97035</span>
</div>
<div class="abs contact-row" style="left:887px;top:3000px">
  <svg width="16" height="16" viewBox="0 0 16 16"><path d="M3 1l3 3-2 2c1 2 3 4 6 6l2-2 3 3-2 2C7 15 1 9 1 3z" fill="#1a8fd6"/></svg>
  <span>503 555 0148</span>
</div>
<div class="abs contact-row" style="left:887px;top:3032px">
  <svg width="16" height="13" viewBox="0 0 16 13"><rect x="0" y="0" width="16" height="13" rx="1.5" fill="#1a8fd6"/><path d="M1 1l7 6 7-6" fill="none" stroke="#050b1a" stroke-width="1.4"/></svg>
  <span>info@harborcrestadvisory.com</span>
</div>

<div class="abs" style="left:60px;top:3103px;width:1080px;height:1px;background:#1c2436"></div>
<p class="abs copyright">©<span>HARBOR CREST ADVISORY</span> -2021 All rights reserved.</p>

</body>
</html>
```